whitening gel shopping website design

Hello:
We would like to create a whitening gel selling website. It will be very close to Glowbrite, but different designs. https://us.glowbriteorals.example/

What is your organization or website name?
Velvet Beaming

Industry: health and beauty
Target user: ladies between 16 to 40, please make the website friendly and lovely

website pages: main website, shop products, enrolled monthly plans, about us, contact us, policy, customer login log out, shopping cart, customer dashboard.

Website main page contains:
1. one slide show that shows advertisements.
2. show current promo codes
3.show a brief overview about our history
4. show a brief overview about the product introduction
5. show a brief overview of our monthly enrolled product plan
6. have an area to show blogs and posts (please take a look at Glowbrite home page)
7. buttons for customer to login, sign up, visit home, about us, policy, returns, subscription etc.

Note: for the contest, please finish the website main page and the product page only, now we don’t have any logo, test or images, please use yours for now.

```html
<!DOCTYPE html>
<html lang="en">
<head>
<meta charset="utf-8">
<title>Velvet Beaming — Teeth Whitening</title>
<link href="https://fonts.googleapis.com/css2?family=Roboto+Condensed:wght@400;700&family=Roboto:wght@400;500;700&display=swap" rel="stylesheet">
<style>
:root{
  --magenta:#c42e7f;
  --magenta-dark:#a8246b;
  --blue:#2188d6;
  --blue-dark:#1b78c0;
  --gold:#e2b22f;
  --ink:#222;
  --text:#777;
  --pale:#eef5fb;
  --white:#fff;
}
*{margin:0;padding:0;box-sizing:border-box}
html,body{width:1200px;height:3488px;overflow:hidden}
body{position:relative;font-family:'Roboto',sans-serif;color:var(--ink);background:var(--white)}
.abs{position:absolute}
.heading{font-family:'Roboto Condensed',sans-serif;font-weight:700;text-transform:uppercase;letter-spacing:.5px}
.label{font-family:'Roboto Condensed',sans-serif;font-size:16px;text-transform:uppercase;color:var(--magenta)}
.body-copy{font-size:13.5px;line-height:29.5px;color:var(--text)}
.btn{display:flex;align-items:center;justify-content:center;gap:8px;background:var(--magenta);color:#fff;font-family:'Roboto Condensed',sans-serif;font-weight:700;font-size:16px;text-transform:uppercase;border-radius:2px}
.btn svg{width:14px;height:14px}
.ghost{font-family:'Roboto Condensed',sans-serif;font-weight:700;color:rgba(0,0,0,.05);text-transform:uppercase;line-height:1}

/* top bar + header */
.topbar{top:0;left:0;width:1200px;height:30px;background:var(--magenta);color:#fff;font-size:12px;display:flex;align-items:center;justify-content:center;letter-spacing:.3px}
.header{top:30px;left:0;width:1200px;height:85px;background:#fff}
.nav{left:144px;top:34px;display:flex;gap:32px;font-size:14px;color:#333}
.brand{left:522px;top:24px;font-family:'Roboto Condensed',sans-serif;font-weight:700;font-size:32px;color:var(--blue);letter-spacing:.3px}
.login{left:813px;top:27px;width:86px;height:32px;border:1px solid #bcd6ee;color:var(--blue);font-size:13px;display:flex;align-items:center;justify-content:center;border-radius:2px}
.signup{left:907px;top:27px;width:86px;height:32px;background:var(--blue);color:#fff;font-size:13px;display:flex;align-items:center;justify-content:center;border-radius:2px}
.cart{left:1014px;top:24px;width:40px;height:40px}

/* hero */
.hero{top:115px;left:0;width:1200px;height:590px}
.hero-photo{position:absolute;inset:0;background:linear-gradient(100deg,#e9d4c7 0%,#dcc6bb 25%,#c9dbe7 48%,#dceaf3 70%,#eaf3f9 100%)}
.hero-title{left:666px;top:148px;font-size:56px;color:#222}
.hero-title span{color:var(--magenta)}
.hero-sub{left:673px;top:222px;font-size:25px;line-height:33px;color:#222;font-weight:500}
.promo{left:673px;top:318px;width:129px;height:44px;background:#9fcce8;border:2px solid #fff;color:#fff;font-family:'Roboto Condensed',sans-serif;font-weight:700;font-size:34px;display:flex;align-items:center;justify-content:center;letter-spacing:1px}
.shop{left:815px;top:318px;width:157px;height:44px}
.dots{left:673px;top:433px;display:flex;gap:8px}
.dots i{width:10px;height:10px;border-radius:50%;background:#fff;display:block}
.dots i.on{background:transparent;border:2px solid #fff}

/* overview */
.overview-bg{top:705px;left:0;width:1200px;height:520px;background:linear-gradient(90deg,#f6efec 0%,#fbf8f7 40%,#fdfcfc 60%,#f8f2f0 100%)}
.circle-photo{left:632px;top:726px;width:420px;height:420px;border-radius:50%;background:radial-gradient(circle at 50% 40%,#f3f7fb 0%,#d8e6f1 60%,#b9d3e8 100%);border:4px solid var(--magenta);border-left-color:transparent;border-top-color:transparent}
.circle-inner{left:632px;top:732px;width:412px;height:412px;border-radius:50%;background:radial-gradient(circle at 50% 40%,#f6f9fc 0%,#dbe8f2 60%,#bfd6e9 100%)}

/* pricing */
.pricing-band{top:1245px;left:0;width:1200px;height:475px;background:var(--magenta)}
.pricing-title{top:1396px;left:0;width:1200px;text-align:center;color:#fff;font-size:44px}
.plan-label{top:1365px;left:0;width:1200px;text-align:center;color:#fff;font-size:16px;font-family:'Roboto Condensed',sans-serif}
.card{background:#fff;box-shadow:0 4px 12px rgba(0,0,0,.12)}
.card-head{position:absolute;left:0;top:0;width:100%;color:#fff;text-align:center;font-size:23px;font-weight:500}
.price{position:absolute;left:50%;transform:translateX(-50%);border-radius:50%;background:#fff;display:flex;align-items:center;justify-content:center;font-weight:700}
.features{position:absolute;list-style:none}
.features li{display:flex;align-items:center;gap:16px;color:#666}
.features svg{width:14px;height:14px;flex:none}
.rule{position:absolute;border-top:1px dashed #ddd}
.details{position:absolute;left:0;width:100%;text-align:center;font-weight:500;font-size:15px}

/* description */
.desc-bg{top:1923px;left:0;width:1200px;height:600px;background:linear-gradient(90deg,#ffffff 0%,#f7f9fb 45%,#fbf1ef 100%)}
.desc-photo{left:0;top:1950px;width:570px;height:515px;background:radial-gradient(ellipse at 35% 55%,#f0f1f3 0%,#e1e4e8 45%,#f7f8fa 75%,rgba(255,255,255,0) 100%)}

/* blog */
.blog-bg{top:2518px;left:0;width:1200px;height:660px;background:linear-gradient(180deg,#ffffff 0%,var(--pale) 100%)}
.post-title{font-family:'Roboto Condensed',sans-serif;font-weight:700;font-size:21px;text-transform:uppercase;color:#222;line-height:24px}
.meta{font-size:11.5px;color:#888;display:flex;gap:14px;align-items:center}
.meta span{display:flex;align-items:center;gap:5px}
.meta svg{width:11px;height:11px}
.excerpt{font-size:11.5px;line-height:20px;color:#888}
.readmore{font-size:12.5px;font-weight:700;color:var(--magenta)}

/* footer */
.footer{top:3165px;left:0;width:1200px;height:280px;background:var(--blue)}
.footer-brand{left:145px;top:3232px;font-family:'Roboto Condensed',sans-serif;font-weight:700;font-size:31px;color:#fff}
.footer h4{position:absolute;font-family:'Roboto Condensed',sans-serif;font-weight:700;font-size:19px;color:#fff;text-transform:uppercase}
.footer-rule{width:14px;height:2px;background:var(--magenta)}
.footer-copy{font-size:13.5px;line-height:25px;color:#fff}
.links{left:519px;top:3284px;list-style:none;font-size:14.5px;color:#fff;line-height:27px}
.socials{left:145px;top:3373px;display:flex;gap:11px}
.socials i{display:block;width:33px;height:33px;border:1.5px solid #fff;border-radius:50%}
.email{left:722px;top:3352px;width:230px;height:40px;background:#fff;font-size:11.5px;color:#555;display:flex;align-items:center;padding-left:16px}
.subscribe{left:952px;top:3352px;width:103px;height:40px;background:var(--magenta);color:#fff;font-weight:500;font-size:15px;display:flex;align-items:center;justify-content:center}
.bottombar{top:3445px;left:0;width:1200px;height:43px;background:var(--blue-dark)}
.copyright{left:145px;top:3460px;font-size:11.5px;color:#fff}
.pay{top:3456px;display:flex;gap:6px;left:904px}
.pay i{display:block;width:32px;height:21px;background:#fff;border-radius:2px}
</style>
</head>
<body>

<div class="abs topbar">FREE SHIPPING ON ALL ORDERS OVER $69 USD</div>

<header class="abs header">
  <nav class="abs nav"><span>HOME</span><span>ABOUT</span><span>PRODUCTS</span></nav>
  <div class="abs brand">VELVET BEAMING</div>
  <div class="abs login">LOGIN</div>
  <div class="abs signup">SIGN UP</div>
  <svg class="abs cart" viewBox="0 0 40 40" fill="none" stroke="#555" stroke-width="2" stroke-linecap="round" stroke-linejoin="round">
    <path d="M2 10h6l5 17h18l4-12H11"/><circle cx="15" cy="33" r="2.5"/><circle cx="29" cy="33" r="2.5"/>
    <circle cx="32" cy="8" r="6" stroke-width="1.5"/><path d="M29.5 8l2 2 3-4" stroke-width="1.5"/>
  </svg>
</header>

<section class="abs hero">
  <div class="hero-photo" role="img" aria-label="Smiling woman applying a whitening pen to her teeth on a soft blue background"></div>
  <svg class="abs" style="left:0;top:520px" width="1200" height="75" viewBox="0 0 1200 75" preserveAspectRatio="none">
    <path d="M0 40 C120 70 300 55 400 52 C440 50 455 62 465 70 C475 62 520 48 600 45 C800 38 1000 60 1200 20 L1200 75 L0 75Z" fill="#fff"/>
    <path d="M0 40 C120 70 300 55 400 52 C440 50 455 62 465 70 C475 62 520 48 600 45 C800 38 1000 60 1200 20" fill="none" stroke="var(--blue)" stroke-width="4"/>
  </svg>
  <div class="abs heading hero-title">VELVET <span>BEAMING</span></div>
  <div class="abs hero-sub">40% Off Bright on Teeth<br>Whitening Products</div>
  <div class="abs promo">F4275</div>
  <div class="abs btn shop">SHOP NOW
    <svg viewBox="0 0 14 14"><circle cx="7" cy="7" r="7" fill="#fff"/><path d="M5.5 4l3 3-3 3" stroke="var(--magenta)" stroke-width="2" fill="none"/></svg>
  </div>
  <div class="abs dots"><i></i><i></i><i class="on"></i><i></i><i></i></div>
</section>

<section>
  <div class="abs overview-bg" role="img" aria-label="Faint background of a smiling mouth with white teeth"></div>
  <div class="abs ghost" style="left:1075px;top:790px;font-size:92px;writing-mode:vertical-rl;transform:rotate(180deg)">ABOUT</div>
  <div class="abs label" style="left:145px;top:764px">HISTORY</div>
  <h2 class="abs heading" style="left:145px;top:793px;font-size:44px">OVERVIEW</h2>
  <p class="abs body-copy" style="left:145px;top:861px;width:420px;text-align:justify">Lorem ipsum dolor sit amet, consectetur adipiscing elit, sed do eiusmod tempor incididunt ut labore et dolore magna aliqua. Ut enim ad minim veniam, quis nostrud exercitation uo It aliquip ex ea commodo consequate irure dolor in reprehenderit in voluptate velit esse cillum dolore eu fugiat nulla pariaturepteur sat cupidatat non proident, sunt in culpa qui officia deserunt mollit anim id est laborum</p>
  <div class="abs btn" style="left:145px;top:1066px;width:157px;height:41px">READ MORE
    <svg viewBox="0 0 14 14"><circle cx="7" cy="7" r="7" fill="#fff"/><path d="M5.5 4l3 3-3 3" stroke="var(--magenta)" stroke-width="2" fill="none"/></svg>
  </div>
  <div class="abs circle-photo"></div>
  <div class="abs circle-inner" role="img" aria-label="Toothpaste tubes, mouthwash bottle and blue toothbrush on a white surface"></div>
</section>

<section>
  <svg class="abs" style="left:0;top:1225px" width="1200" height="50" viewBox="0 0 1200 50" preserveAspectRatio="none">
    <path d="M0 50 L0 30 C120 5 300 20 500 25 C620 28 690 30 733 8 C780 30 900 30 1000 22 C1100 14 1160 18 1200 30 L1200 50Z" fill="var(--magenta)"/>
    <path d="M0 30 C120 5 300 20 500 25 C620 28 690 30 733 8 C780 30 900 30 1000 22 C1100 14 1160 18 1200 30" fill="none" stroke="var(--blue)" stroke-width="4"/>
  </svg>
  <div class="abs pricing-band"></div>
  <div class="abs" style="left:0;top:1720px;width:1200px;height:210px;background:linear-gradient(90deg,#fbfcfd 0%,#fbf5f3 100%)" role="img" aria-label="Faint background of a smiling mouth"></div>
  <div class="abs ghost" style="left:88px;top:1318px;font-size:96px;color:rgba(255,255,255,.1)">PRICING</div>
  <div class="abs plan-label">PLAN</div>
  <h2 class="abs heading pricing-title">OUR PRICING</h2>

  <div class="abs card" style="left:196px;top:1510px;width:251px;height:386px">
    <div class="card-head" style="height:115px;background:var(--blue);padding-top:18px">Basic Plan</div>
    <div class="price" style="top:70px;width:92px;height:92px;border:4px solid var(--blue);color:var(--blue);font-size:29px">$12</div>
    <ul class="features" style="left:26px;top:188px;font-size:13.5px;line-height:31.5px">
      <li><svg viewBox="0 0 14 14"><path d="M2 7l3.5 3.5L12 3" stroke="var(--blue)" stroke-width="2.4" fill="none"/></svg>Iusto odio dignissimos</li>
      <li><svg viewBox="0 0 14 14"><path d="M2 7l3.5 3.5L12 3" stroke="var(--blue)" stroke-width="2.4" fill="none"/></svg>Voluptatum deleniti</li>
      <li><svg viewBox="0 0 14 14"><path d="M2 7l3.5 3.5L12 3" stroke="var(--blue)" stroke-width="2.4" fill="none"/></svg>Omnis dolor repellendus</li>
      <li><svg viewBox="0 0 14 14"><path d="M2 7l3.5 3.5L12 3" stroke="var(--blue)" stroke-width="2.4" fill="none"/></svg>Repudiandae sint</li>
    </ul>
    <div class="rule" style="left:12px;right:12px;top:333px"></div>
    <div class="details" style="top:352px;color:var(--blue)">View Details &nbsp;»</div>
  </div>

  <div class="abs card" style="left:751px;top:1510px;width:251px;height:386px">
    <div class="card-head" style="height:115px;background:var(--blue);padding-top:18px">Professional Plan</div>
    <div class="price" style="top:70px;width:92px;height:92px;border:4px solid var(--blue);color:var(--blue);font-size:29px">$12</div>
    <ul class="features" style="left:26px;top:188px;font-size:13.5px;line-height:31.5px">
      <li><svg viewBox="0 0 14 14"><path d="M2 7l3.5 3.5L12 3" stroke="var(--blue)" stroke-width="2.4" fill="none"/></svg>Iusto odio dignissimos</li>
      <li><svg viewBox="0 0 14 14"><path d="M2 7l3.5 3.5L12 3" stroke="var(--blue)" stroke-width="2.4" fill="none"/></svg>Voluptatum deleniti</li>
      <li><svg viewBox="0 0 14 14"><path d="M2 7l3.5 3.5L12 3" stroke="var(--blue)" stroke-width="2.4" fill="none"/></svg>Omnis dolor repellendus</li>
      <li><svg viewBox="0 0 14 14"><path d="M2 7l3.5 3.5L12 3" stroke="var(--blue)" stroke-width="2.4" fill="none"/></svg>Repudiandae sint</li>
    </ul>
    <div class="rule" style="left:12px;right:12px;top:333px"></div>
    <div class="details" style="top:352px;color:var(--blue)">View Details &nbsp;»</div>
  </div>

  <div class="abs card" style="left:447px;top:1483px;width:304px;height:440px;z-index:2">
    <div class="card-head" style="height:131px;background:var(--gold);padding-top:24px;font-size:24px">Standard Plan</div>
    <div class="price" style="top:77px;width:108px;height:108px;border:4px solid var(--gold);color:var(--gold);font-size:37px">$12</div>
    <ul class="features" style="left:46px;top:210px;font-size:16px;line-height:36.5px">
      <li><svg viewBox="0 0 14 14"><path d="M2 7l3.5 3.5L12 3" stroke="var(--gold)" stroke-width="2.4" fill="none"/></svg>Iusto odio dignissimos</li>
      <li><svg viewBox="0 0 14 14"><path d="M2 7l3.5 3.5L12 3" stroke="var(--gold)" stroke-width="2.4" fill="none"/></svg>Voluptatum deleniti</li>
      <li><svg viewBox="0 0 14 14"><path d="M2 7l3.5 3.5L12 3" stroke="var(--gold)" stroke-width="2.4" fill="none"/></svg>Omnis dolor repellendus</li>
      <li><svg viewBox="0 0 14 14"><path d="M2 7l3.5 3.5L12 3" stroke="var(--gold)" stroke-width="2.4" fill="none"/></svg>Repudiandae sint</li>
    </ul>
    <div class="rule" style="left:14px;right:14px;top:380px"></div>
    <div class="details" style="top:398px;color:var(--gold);font-size:17px">View Details &nbsp;»</div>
  </div>
</section>

<section>
  <div class="abs desc-bg" role="img" aria-label="Faint background of a smiling mouth with white teeth"></div>
  <div class="abs desc-photo" role="img" aria-label="Squeezed white toothpaste tube and a blue whitening mouth tray"></div>
  <div class="abs ghost" style="left:488px;top:1930px;font-size:92px;writing-mode:vertical-rl;transform:rotate(180deg)">DESCRIPTION</div>
  <div class="abs label" style="left:588px;top:2085px">PRODUCT</div>
  <h2 class="abs heading" style="left:588px;top:2114px;font-size:44px">DESCRIPTION</h2>
  <p class="abs body-copy" style="left:588px;top:2178px;width:420px;text-align:justify">Lorem ipsum dolor sit amet, consectetur adipiscing elit, sed do eiusmod tempor incididunt ut labore et dolore magna aliqua. Ut enim ad minim veniam, quis nostrud exercitation uo It aliquip ex ea commodo consequate irure doloit in voluptate</p>
  <div class="abs btn" style="left:588px;top:2321px;width:157px;height:41px">READ MORE
    <svg viewBox="0 0 14 14"><circle cx="7" cy="7" r="7" fill="#fff"/><path d="M5.5 4l3 3-3 3" stroke="var(--magenta)" stroke-width="2" fill="none"/></svg>
  </div>
</section>

<section>
  <div class="abs blog-bg"></div>
  <div class="abs ghost" style="left:0;top:3010px;font-size:92px">BLOG</div>
  <div class="abs label" style="left:148px;top:2703px">LATEST BLOG</div>
  <h2 class="abs heading" style="left:148px;top:2735px;font-size:44px">FROM THE BLOG</h2>
  <p class="abs body-copy" style="left:148px;top:2800px;width:330px">Lorem ipsum dolor sit amet, consectetur adipiscing elit, sed do eiusmod tempor incididunt ut labore et dolore magna aliqquate irure doloit in voluptate</p>
  <div class="abs btn" style="left:149px;top:2918px;width:193px;height:41px">EXPLORE THE BLOG
    <svg viewBox="0 0 14 14"><circle cx="7" cy="7" r="7" fill="#fff"/><path d="M5.5 4l3 3-3 3" stroke="var(--magenta)" stroke-width="2" fill="none"/></svg>
  </div>

  <div class="abs" style="left:521px;top:2635px;width:230px;height:235px;background:linear-gradient(135deg,#d9b59d 0%,#c39a84 45%,#7d74c9 70%,#b98f78 100%)" role="img" aria-label="Person using a blue light teeth whitening device"></div>
  <div class="abs post-title" style="left:521px;top:2893px">BLOG TITLE HERE</div>
  <div class="abs meta" style="left:521px;top:2932px">
    <span><svg viewBox="0 0 12 12"><circle cx="6" cy="6" r="5" stroke="var(--blue)" stroke-width="1.5" fill="none"/><path d="M6 3v3h2" stroke="var(--blue)" stroke-width="1.5" fill="none"/></svg>4 min read</span>
    <span><svg viewBox="0 0 12 12"><rect x="1" y="2" width="10" height="9" stroke="var(--magenta)" stroke-width="1.5" fill="none"/><path d="M1 5h10" stroke="var(--magenta)" stroke-width="1.5"/></svg>Feb 20, 2019</span>
  </div>
  <p class="abs excerpt" style="left:521px;top:2955px;width:230px">Lorem ipsum dolor sit amet, consectetur adipul labore et dolore magna aliqua. consequate irureo voluptate</p>
  <div class="abs readmore" style="left:521px;top:3030px">Read More &gt;&gt;</div>

  <div class="abs" style="left:781px;top:2635px;width:144px;height:113px;background:linear-gradient(135deg,#efe2da 0%,#d9b9a6 50%,#c9a08a 100%)" role="img" aria-label="Smiling woman portrait"></div>
  <div class="abs post-title" style="left:941px;top:2641px">BLOG TITLE<br>HERE</div>
  <div class="abs meta" style="left:941px;top:2705px;flex-direction:column;align-items:flex-start;gap:4px">
    <span><svg viewBox="0 0 12 12"><circle cx="6" cy="6" r="5" stroke="var(--blue)" stroke-width="1.5" fill="none"/><path d="M6 3v3h2" stroke="var(--blue)" stroke-width="1.5" fill="none"/></svg>4 min read</span>
    <span><svg viewBox="0 0 12 12"><rect x="1" y="2" width="10" height="9" stroke="var(--magenta)" stroke-width="1.5" fill="none"/><path d="M1 5h10" stroke="var(--magenta)" stroke-width="1.5"/></svg>Feb 20, 2019</span>
  </div>
  <p class="abs excerpt" style="left:781px;top:2760px;width:230px">Lorem ipsum dolor sit amet, consectetur adiput labore et dolore magna aliqua.</p>
  <div class="abs readmore" style="left:781px;top:2810px">Read More &gt;&gt;</div>

  <div class="abs" style="left:781px;top:2857px;width:144px;height:113px;background:linear-gradient(135deg,#cfdbe6 0%,#dcbba6 50%,#c79c84 100%)" role="img" aria-label="Smiling woman in a dental chair"></div>
  <div class="abs post-title" style="left:941px;top:2862px">BLOG TITLE<br>HERE</div>
  <div class="abs meta" style="left:941px;top:2926px;flex-direction:column;align-items:flex-start;gap:4px">
    <span><svg viewBox="0 0 12 12"><circle cx="6" cy="6" r="5" stroke="var(--blue)" stroke-width="1.5" fill="none"/><path d="M6 3v3h2" stroke="var(--blue)" stroke-width="1.5" fill="none"/></svg>4 min read</span>
    <span><svg viewBox="0 0 12 12"><rect x="1" y="2" width="10" height="9" stroke="var(--magenta)" stroke-width="1.5" fill="none"/><path d="M1 5h10" stroke="var(--magenta)" stroke-width="1.5"/></svg>Feb 20, 2019</span>
  </div>
  <p class="abs excerpt" style="left:781px;top:2981px;width:230px">Lorem ipsum dolor sit amet, consectetur adiput labore et dolore magna aliqua.</p>
  <div class="abs readmore" style="left:781px;top:3030px">Read More &gt;&gt;</div>
</section>

<footer>
  <div class="abs footer"></div>
  <svg class="abs" style="left:0;top:3135px" width="1200" height="45" viewBox="0 0 1200 45" preserveAspectRatio="none">
    <path d="M0 45 L0 30 C150 35 350 10 480 15 C520 17 535 28 540 32 C545 28 560 17 600 15 C800 8 1000 35 1200 20 L1200 45Z" fill="var(--blue)"/>
    <path d="M0 30 C150 35 350 10 480 15 C520 17 535 28 540 32 C545 28 560 17 600 15 C800 8 1000 35 1200 20" fill="none" stroke="var(--magenta)" stroke-width="4"/>
  </svg>
  <div class="abs footer-brand">VELVET BEAMING</div>
  <p class="abs footer-copy" style="left:145px;top:3285px;width:310px">Lorem ipsum dolor sit amet, consectetur adipiscing elit, sed do eiusmod tempor incididunt ut labore et dolore magna aliqua irure doloit in voluptate</p>
  <div class="abs socials"><i></i><i></i><i></i><i></i></div>

  <h4 style="left:519px;top:3237px">QUICK LINKS</h4>
  <div class="abs footer-rule" style="left:519px;top:3267px"></div>
  <ul class="abs links"><li>Visit home</li><li>About us</li><li>Policy</li><li>Returns</li></ul>

  <h4 style="left:719px;top:3237px">SUBSCRIBE TO NEWSLETTER</h4>
  <div class="abs footer-rule" style="left:719px;top:3267px"></div>
  <p class="abs footer-copy" style="left:719px;top:3284px;font-size:14.5px">Lorem ipsum dolor sit amet, consectetur</p>
  <div class="abs email">Enter Email</div>
  <div class="abs subscribe">SUBSCRIBE</div>

  <div class="abs bottombar"></div>
  <div class="abs copyright">© copyright 2019 Velvet Beaming. All Rights Reserved &nbsp;| &nbsp;Privacy policy</div>
  <div class="abs pay"><i></i><i></i><i></i><i></i></div>
</footer>

</body>
</html>
```